Real Estate Seller Financing Postcard

I need a postcard that lays out these options contained in the notes that grabs attention, explains the two options easily and is eye-catching. The front needs to have the percentages on it and information about it and on the other side One side exact Text is:
"Monthly income without tenant headaches" in big letters. Also on front "Get
110%
add an "or"
160% of market value for your property. ". The percentages should be displayed and that is not to be a sentence of text. Other side text: I need bullets points for these "Formal protection as a lien holder against home
No commission or closing cost
Fast closings possible
Property taken as is so no repairs.

Add to the top of the back in "It’s simple. I am a new investor without down payment capital who still want to double our portfolio this year to grow our portfolio."
Here are the two options that are to be the largest part of the back
Option 1, you can receive 80% now cash and 30% over a short period of time including interest.

Option 2, where act like a bank allowing you to make 150% if you finance the whole property(ies). No gimmicks and surprises, just simple unconventional financing.

Include Logo Somewhere

Target Market(s)

Property Owners Wanting to Sell Their Property

Industry/Entity Type

Real Estate Investing

Requirements
Must have
• The options promiment and each side with its respective information. Must have logo somewhere
Nice to have
• The options in color other than black.
Should not have
• A picture of money on the front. Any other image is okay.

```html
<!DOCTYPE html>
<html lang="en">
<head>
<meta charset="utf-8">
<title>Seller Financing Postcards – Meridian Real Estate Group</title>
<link rel="stylesheet" href="https://fonts.googleapis.com/css2?family=Anton&family=Montserrat:ital,wght@0,400;0,500;0,700;0,900;1,900&family=Oswald:wght@300;500;700&family=Poppins:ital,wght@0,300;0,600;1,300;1,600;1,700&family=Roboto:wght@700&display=swap">
<style>
  :root{
    --page:#d9d9d9;
    --navy:#0a2463;
    --navy-deep:#061a4d;
    --blue:#1a4aa6;
    --blue-bright:#2e6ae0;
    --band:#0b5cab;
    --silver-hi:#f7f7f8;
    --silver-lo:#b5b9c1;
    --grey-text:#6b6d72;
    --white:#ffffff;
  }
  *{box-sizing:border-box;margin:0;padding:0}
  html,body{width:1200px;height:868px;overflow:hidden;background:var(--page)}
  .sheet{position:relative;width:1200px;height:868px}
  .card{position:absolute;width:512px;height:348px;overflow:hidden;background:var(--white)}
  .card--front-a{left:77px;top:65px}
  .card--back-a{left:611px;top:65px}
  .card--front-b{left:77px;top:455px}
  .card--back-b{left:611px;top:455px}
  .card-bg{position:absolute;inset:0;width:512px;height:348px}
  .abs{position:absolute;white-space:nowrap}
  .squeeze{transform-origin:left top}

  /* brand */
  .brand{position:absolute;display:flex;align-items:center;gap:10px}
  .brand-dot{width:48px;height:48px;border-radius:50%;border:2px solid var(--blue);flex:none}
  .brand-name{font-family:"Montserrat",sans-serif;font-weight:500;color:var(--blue);line-height:1;white-space:nowrap}
  .brand-name .big{display:block;font-size:18px;letter-spacing:0}
  .brand-name .small{display:block;font-size:8.6px;margin-top:4px}

  /* front headline */
  .hl-make{font-family:"Montserrat",sans-serif;font-weight:900;font-style:italic;font-size:50px;color:var(--navy);letter-spacing:-1px}
  .hl-money{font-family:"Anton",sans-serif;font-size:112px;line-height:1;letter-spacing:-1px;transform:skewX(-10deg);transform-origin:left bottom;
    background:linear-gradient(100deg,var(--navy) 30%,var(--blue-bright) 55%,var(--navy) 80%);
    -webkit-background-clip:text;background-clip:text;color:transparent}
  .hl-likea{font-family:"Oswald",sans-serif;font-weight:500;font-size:48px;line-height:1;color:var(--grey-text);transform:scaleX(.88)}
  .hl-bank{font-family:"Roboto",sans-serif;font-weight:700;font-size:45px;line-height:1;color:var(--blue)}
  .divider{position:absolute;width:2px;background:#555}

  .pct-get{font-family:"Anton",sans-serif;font-size:60px;line-height:1;transform:skewX(-8deg);
    background:linear-gradient(#fff,#9ea3ab);-webkit-background-clip:text;background-clip:text;color:transparent}
  .pill{position:absolute;border-radius:16px;transform:skewX(-8deg);
    background:linear-gradient(#fafafa,var(--silver-lo));box-shadow:0 3px 6px rgba(0,0,0,.35);
    display:flex;align-items:center;justify-content:center}
  .pill span{font-family:"Montserrat",sans-serif;font-weight:900;font-style:italic;color:var(--navy);letter-spacing:-1px}
  .pill .huge{font-family:"Anton",sans-serif;font-style:normal;font-weight:400;font-size:92px;letter-spacing:0;
    background:linear-gradient(100deg,var(--navy) 30%,var(--blue-bright) 55%,var(--navy) 80%);
    -webkit-background-clip:text;background-clip:text;color:transparent}
  .pct-or{font-family:"Anton",sans-serif;font-size:58px;line-height:1;color:var(--navy);transform:skewX(-8deg)}

  .mv-line{font-family:"Oswald",sans-serif;font-weight:300;color:var(--white);line-height:1}
  .mv-strong{font-family:"Anton",sans-serif;color:var(--white);line-height:1}

  .perks{position:absolute;left:274px;top:222px;list-style:none;font-family:"Montserrat",sans-serif;font-size:10.5px;color:var(--white)}
  .perks li{position:absolute;left:0;display:flex;gap:6px;line-height:12px;white-space:nowrap}
  .perks svg{width:18px;height:16px;flex:none;margin-top:-4px}

  .hl-monthly{font-family:"Oswald",sans-serif;font-weight:300;font-size:37px;line-height:1;color:#1d1d1f;letter-spacing:-1px;transform:scaleX(.9)}
  .hl-without{font-family:"Oswald",sans-serif;font-weight:700;font-size:33px;line-height:1;color:var(--grey-text);letter-spacing:-1px;transform:scaleX(.93)}
  .hl-headaches{font-family:"Roboto",sans-serif;font-weight:700;font-size:34px;line-height:1;color:var(--blue);letter-spacing:1px}
  .rule{position:absolute;height:2px;background:var(--navy)}

  /* back */
  .intro{position:absolute;left:20px;top:24px;font-family:"Poppins",sans-serif;font-weight:600;font-size:11.4px;line-height:13.6px;color:var(--white)}
  .intro .lead{font-weight:300;font-size:15px}
  .tab{position:absolute;border-radius:10px;background:linear-gradient(#fbfbfb,var(--silver-lo));
    font-family:"Montserrat",sans-serif;font-weight:900;font-style:italic;color:var(--navy);
    display:flex;align-items:center;justify-content:center;box-shadow:0 2px 4px rgba(0,0,0,.35);transform:skewX(-8deg)}
  .tab span{transform:skewX(8deg)}
  .panel{position:absolute;border:1.5px solid rgba(190,210,255,.75);border-radius:14px}
  .tick-dot{position:absolute;width:18px;height:18px}
  .panel-text{position:absolute;font-family:"Poppins",sans-serif;font-weight:300;font-style:italic;color:var(--white);white-space:nowrap}
  .panel-text b{font-weight:700;color:#cfe0ff}
  .icon-slot{position:absolute;width:68px;height:68px;border-radius:50%;
    background:radial-gradient(circle at 40% 35%,#ffffff,#b3b7bf 70%,#8c9099);box-shadow:0 3px 6px rgba(0,0,0,.4)}
  .stamp{position:absolute;left:432px;top:21px;width:60px;height:60px;border:1.5px solid #111}
  .addr{position:absolute;left:289px;width:223px;height:1px;background:#111}
</style>
</head>
<body>
<main class="sheet">

  <!-- Front: make money like a bank -->
  <section class="card card--front-a">
    <svg class="card-bg" viewBox="0 0 512 348" aria-hidden="true">
      <defs>
        <linearGradient id="bandA" x1="0" y1="0" x2="1" y2="1">
          <stop offset="0" stop-color="#0a2463"/><stop offset=".5" stop-color="#1a3d8f"/><stop offset="1" stop-color="#061a4d"/>
        </linearGradient>
        <linearGradient id="silverA" x1="0" y1="0" x2="0" y2="1">
          <stop offset="0" stop-color="#ffffff"/><stop offset=".6" stop-color="#e9eaec"/><stop offset="1" stop-color="#cfd2d7"/>
        </linearGradient>
      </defs>
      <rect width="512" height="348" fill="#fff"/>
      <rect y="188" width="512" height="160" fill="url(#bandA)"/>
      <ellipse cx="135" cy="96" rx="192" ry="112" fill="#2e6ae0"/>
      <ellipse cx="135" cy="92" rx="190" ry="112" fill="#1a4aa6"/>
      <ellipse cx="135" cy="88" rx="190" ry="112" fill="url(#silverA)"/>
    </svg>

    <div class="abs hl-make" style="left:29px;top:24px">MAKE</div>
    <div class="abs hl-money" style="left:30px;top:72px">MONEY</div>

    <div class="brand" style="left:329px;top:21px">
      <div class="brand-dot"></div>
      <div class="brand-name"><span class="big">MERIDIAN</span><span class="small">REAL ESTATE GROUP</span></div>
    </div>

    <div class="divider" style="left:338px;top:104px;height:72px"></div>
    <div class="abs hl-likea squeeze" style="left:351px;top:101px">LIKE A</div>
    <div class="abs hl-bank" style="left:351px;top:141px">BANK</div>

    <div class="abs pct-get" style="left:22px;top:220px">GET</div>
    <div class="pill" style="left:105px;top:221px;width:127px;height:58px"><span style="font-size:40px">160%</span></div>
    <div class="abs mv-line" style="left:43px;top:286px;font-size:22px">OF MARKET VALUE FOR</div>
    <div class="abs mv-strong" style="left:50px;top:307px;font-size:26px">YOUR PROPERTY.</div>

    <ul class="perks">
      <li style="top:0"><svg viewBox="0 0 18 16" aria-hidden="true"><path d="M1 9l5 5L17 1" fill="none" stroke="#4f8cff" stroke-width="3"/></svg><span>Formal protection as a lien holder<br>against home</span></li>
      <li style="top:37px"><svg viewBox="0 0 18 16" aria-hidden="true"><path d="M1 9l5 5L17 1" fill="none" stroke="#4f8cff" stroke-width="3"/></svg><span>No commission or closing cost</span></li>
      <li style="top:60px"><svg viewBox="0 0 18 16" aria-hidden="true"><path d="M1 9l5 5L17 1" fill="none" stroke="#4f8cff" stroke-width="3"/></svg><span>Fast closings possible</span></li>
      <li style="top:83px"><svg viewBox="0 0 18 16" aria-hidden="true"><path d="M1 9l5 5L17 1" fill="none" stroke="#4f8cff" stroke-width="3"/></svg><span>Property taken as is so no repairs.</span></li>
    </ul>
  </section>

  <!-- Back: how it works -->
  <section class="card card--back-a">
    <svg class="card-bg" viewBox="0 0 512 348" aria-hidden="true">
      <defs>
        <linearGradient id="backA" x1="0" y1="0" x2="1" y2="1">
          <stop offset="0" stop-color="#0a2463"/><stop offset=".5" stop-color="#1a4aa6"/><stop offset="1" stop-color="#061a4d"/>
        </linearGradient>
      </defs>
      <rect width="512" height="348" fill="url(#backA)"/>
      <rect y="20" width="340" height="68" fill="#0b5cab"/>
      <path d="M340 0 Q200 174 326 348 L512 348 L512 0Z" fill="#2e6ae0"/>
      <path d="M348 0 Q212 174 334 348 L512 348 L512 0Z" fill="#9ea3ab"/>
      <path d="M354 0 Q220 174 340 348 L512 348 L512 0Z" fill="#fff"/>
    </svg>

    <p class="intro"><span class="lead">It’s simple. </span>I am a new investor without<br>down payment capital who still want<br>to double our portfolio this year to<br>grow my portfolio.</p>

    <div class="panel" style="left:15px;top:113px;width:225px;height:114px"></div>
    <div class="tab" style="left:32px;top:97px;width:140px;height:26px;font-size:18px"><span>How it works</span></div>
    <svg class="tick-dot" style="left:10px;top:132px" viewBox="0 0 18 18" aria-hidden="true"><circle cx="9" cy="9" r="8" fill="#1a4aa6" stroke="#cfe0ff" stroke-width="1.5"/><path d="M5 9l3 3 5-6" fill="none" stroke="#fff" stroke-width="1.8"/></svg>
    <p class="panel-text" style="left:34px;top:126px;font-size:13px;line-height:15px">where act like a bank allowing<br>you to make <b style="font-size:16px">160%</b> if you<br>finance the whole property(ies).<br>No gimmicks and surprises,<br>just simple unconventional<br>financing.</p>

    <div class="icon-slot" style="left:23px;top:248px" role="img" aria-label="Illustration of an office building with a rising arrow"></div>
    <div class="icon-slot" style="left:103px;top:248px" role="img" aria-label="Illustration of a house balanced against coins on a seesaw"></div>
    <div class="icon-slot" style="left:184px;top:248px" role="img" aria-label="Illustration of a house with coins and a payment card"></div>

    <div class="stamp"></div>
    <div class="addr" style="top:209px"></div>
    <div class="addr" style="top:237px"></div>
    <div class="addr" style="top:263px"></div>
    <div class="addr" style="top:289px"></div>
  </section>

  <!-- Front: 110% or 160% -->
  <section class="card card--front-b">
    <svg class="card-bg" viewBox="0 0 512 348" aria-hidden="true">
      <defs>
        <linearGradient id="bandB" x1="0" y1="0" x2="1" y2="1">
          <stop offset="0" stop-color="#0a2463"/><stop offset=".5" stop-color="#1a3d8f"/><stop offset="1" stop-color="#061a4d"/>
        </linearGradient>
        <linearGradient id="silverB" x1="0" y1="0" x2="0" y2="1">
          <stop offset="0" stop-color="#ffffff"/><stop offset=".6" stop-color="#e9eaec"/><stop offset="1" stop-color="#cfd2d7"/>
        </linearGradient>
      </defs>
      <rect width="512" height="348" fill="#fff"/>
      <rect y="189" width="512" height="159" fill="url(#bandB)"/>
      <ellipse cx="80" cy="118" rx="199" ry="135" fill="#2e6ae0"/>
      <ellipse cx="80" cy="114" rx="197" ry="135" fill="#1a4aa6"/>
      <ellipse cx="80" cy="110" rx="197" ry="135" fill="url(#silverB)"/>
    </svg>

    <div class="abs hl-make" style="left:21px;top:12px;font-size:52px">GET</div>
    <div class="pill" style="left:21px;top:71px;width:206px;height:95px"><span class="huge">110%</span></div>
    <div class="abs pct-or" style="left:47px;top:172px">OR</div>
    <div class="pill" style="left:105px;top:174px;width:123px;height:58px"><span style="font-size:39px">160%</span></div>

    <div class="abs mv-line" style="left:31px;top:263px;font-size:25px">OF MARKET VALUE FOR</div>
    <div class="abs mv-strong" style="left:40px;top:287px;font-size:30px">YOUR PROPERTY.</div>

    <div class="brand" style="left:317px;top:20px">
      <div class="brand-dot" style="width:51px;height:51px"></div>
      <div class="brand-name"><span class="big" style="font-size:18.5px">MERIDIAN</span><span class="small">REAL ESTATE GROUP</span></div>
    </div>

    <div class="abs hl-monthly squeeze" style="left:297px;top:80px">MONTHLY INCOME</div>
    <div class="abs hl-without squeeze" style="left:289px;top:114px">WITHOUT TENANT</div>
    <div class="abs hl-headaches" style="left:286px;top:145px">HEADACHES</div>
    <div class="rule" style="left:265px;top:178px;width:227px"></div>

    <ul class="perks">
      <li style="top:0"><svg viewBox="0 0 18 16" aria-hidden="true"><path d="M1 9l5 5L17 1" fill="none" stroke="#4f8cff" stroke-width="3"/></svg><span>Formal protection as a lien holder<br>against home</span></li>
      <li style="top:37px"><svg viewBox="0 0 18 16" aria-hidden="true"><path d="M1 9l5 5L17 1" fill="none" stroke="#4f8cff" stroke-width="3"/></svg><span>No commission or closing cost</span></li>
      <li style="top:60px"><svg viewBox="0 0 18 16" aria-hidden="true"><path d="M1 9l5 5L17 1" fill="none" stroke="#4f8cff" stroke-width="3"/></svg><span>Fast closings possible</span></li>
      <li style="top:83px"><svg viewBox="0 0 18 16" aria-hidden="true"><path d="M1 9l5 5L17 1" fill="none" stroke="#4f8cff" stroke-width="3"/></svg><span>Property taken as is so no repairs.</span></li>
    </ul>
  </section>

  <!-- Back: two options -->
  <section class="card card--back-b">
    <svg class="card-bg" viewBox="0 0 512 348" aria-hidden="true">
      <defs>
        <linearGradient id="backB" x1="0" y1="0" x2="1" y2="1">
          <stop offset="0" stop-color="#0a2463"/><stop offset=".5" stop-color="#1a4aa6"/><stop offset="1" stop-color="#061a4d"/>
        </linearGradient>
      </defs>
      <rect width="512" height="348" fill="url(#backB)"/>
      <rect y="20" width="330" height="68" fill="#0b5cab"/>
      <path d="M324 0 Q192 174 314 348 L512 348 L512 0Z" fill="#2e6ae0"/>
      <path d="M332 0 Q202 174 322 348 L512 348 L512 0Z" fill="#9ea3ab"/>
      <path d="M338 0 Q210 174 328 348 L512 348 L512 0Z" fill="#fff"/>
    </svg>

    <p class="intro"><span class="lead">It’s simple. </span>I am a new investor without<br>down payment capital who still want<br>to double our portfolio this year to<br>grow my portfolio.</p>

    <div class="panel" style="left:14px;top:117px;width:220px;height:54px"></div>
    <div class="tab" style="left:31px;top:102px;width:110px;height:28px;font-size:19px"><span>OPTION 1</span></div>
    <svg class="tick-dot" style="left:10px;top:131px" viewBox="0 0 18 18" aria-hidden="true"><circle cx="9" cy="9" r="8" fill="#1a4aa6" stroke="#cfe0ff" stroke-width="1.5"/><path d="M5 9l3 3 5-6" fill="none" stroke="#fff" stroke-width="1.8"/></svg>
    <p class="panel-text" style="left:32px;top:130px;font-size:11px;line-height:10.5px">you can receive <b style="font-size:12px">80%</b> now cash and<br><b style="font-size:12px">30%</b> over a short period of time<br>including interest.</p>

    <div class="panel" style="left:14px;top:200px;width:220px;height:108px"></div>
    <div class="tab" style="left:31px;top:184px;width:110px;height:28px;font-size:19px"><span>OPTION 2</span></div>
    <svg class="tick-dot" style="left:10px;top:215px" viewBox="0 0 18 18" aria-hidden="true"><circle cx="9" cy="9" r="8" fill="#1a4aa6" stroke="#cfe0ff" stroke-width="1.5"/><path d="M5 9l3 3 5-6" fill="none" stroke="#fff" stroke-width="1.8"/></svg>
    <p class="panel-text" style="left:32px;top:215px;font-size:9.5px;line-height:10.1px">Seller financing is where you act like a<br>bank allowing to earn <b style="font-size:10.5px">150%</b> of your<br>property’s value with the inclusion of<br>interest as you will be paid for the property<br>just like a mortgage holder. No gimmicks<br>or surprises, just payments monthly<br>without the headache of tenants while<br>earning interest on your property.</p>

    <div class="stamp"></div>
    <div class="addr" style="top:209px"></div>
    <div class="addr" style="top:237px"></div>
    <div class="addr" style="top:263px"></div>
    <div class="addr" style="top:289px"></div>
  </section>

</main>
</body>
</html>
```